Harbo Hale - A non profit for healthy lifestyle and fitness within refugee camps

We need a logo and website design for a new 501c3 Non-Profit based in San Francisco called 'Harbo Hale'. We help coordinate trips across the globe to provide fitness classes to refugee camps to help refugees maintain a healthy lifestyle and fun while exercising.
Our first trip was to Greece and we hope to extend our reach by working with other non-profits to coordinate how we can help bring a healthy lifestyle and a wellness to refugees in need.
We would like to see website design that use the color green and blue. The final design should represent a welcoming website to encourage people to take a trip either by themselves, as a group, or with a corporate team.
We have 3 certified and experienced trainers that will be running these trips and with a hope of 20 volunteers per trip to help.

We are hoping to partner with another 501c3 called 'Tide to Dawn' which I have participated in and with the hopes of providing an easier and simpler user experience than their current website but with many of the same content.

We would like a 'Trips' page with previous trips, 'Trainers/Hosts' page with bios of the leaders hosting the event, 'Register Page' for folks to register for upcoming trips, 'About Us' page for our mission statement and work, 'Albums' page for photos taken on the trip, 'Contact Us' page for FAQs and questions to submit, and a 'Donate' page for people to donate to our cause.

I would like this page to be created in Word Press.

ie: http://www.tidetodawn-example.com.au/programs/

Target Market(s)

Volunteers, non-profit partners

Industry/Entity Type

Non-Profit

Number of Pages Required

4 page

Font styles to use
Sans Serif

Colors

Designer to choose colors to be used in the design.

Requirements
Must have
• 'Trips' page with previous trips, 'Trainers/Hosts' page with bios of the leaders hosting the event, 'Register Page' for folks to register for upcoming trips, 'About Us' page for our mission statement and work, 'Albums' page for photos taken on the trip, 'Contact Us' page for FAQs and questions to submit, and a 'Donate' page for people to donate to our cause.

```html
<!DOCTYPE html>
<html lang="en">
<head>
<meta charset="utf-8">
<title>Harbo Hale</title>
<link href="https://fonts.googleapis.com/css2?family=Montserrat:wght@400;500;600;700;800&display=swap" rel="stylesheet">
<style>
:root{
  --green:#6dbe45;
  --navy:#2f2a78;
  --navy-deep:#26226a;
  --ink:#1c1c1c;
  --muted:#555;
  --dark:#2a2a2a;
  --darker:#1f1f1f;
  --card:#6a6a6a;
  --white:#fff;
}
*{box-sizing:border-box;margin:0;padding:0}
html,body{width:1200px;height:3321px;overflow:hidden}
body{font-family:'Montserrat',sans-serif;color:var(--ink);background:var(--white);position:relative}

/* top bar */
.topbar{position:absolute;left:0;top:0;width:1200px;height:27px;background:var(--darker);color:#ddd;font-size:10px}
.topbar .tag{position:absolute;left:162px;top:8px}
.topbar .phone{position:absolute;left:805px;top:8px}
.topbar .social{position:absolute;left:882px;top:0;display:flex}
.topbar .social span{width:32px;height:27px;display:block}
.s1{background:#333}.s2{background:#c0392b}.s3{background:#3b5998}.s4{background:#9c5b3b}

/* nav */
.nav{position:absolute;left:0;top:27px;width:1200px;height:73px;background:var(--white)}
.brand{position:absolute;left:162px;top:20px;display:flex;align-items:center;gap:10px;font-weight:800;font-size:24px;color:var(--navy)}
.brand i{width:22px;height:22px;background:var(--green);display:block}
.menu{position:absolute;right:162px;top:30px;display:flex;gap:28px;font-size:12.5px;font-weight:500;color:#222}

/* hero */
.hero{position:absolute;left:0;top:100px;width:1200px;height:465px;
  background:linear-gradient(100deg,#4b5560 0%,#5f6f5c 40%,#7c9a55 70%,#9aa27a 100%)}
.hero .shade{position:absolute;inset:0;background:linear-gradient(90deg,rgba(30,35,40,.55) 0%,rgba(30,35,40,.2) 55%,rgba(0,0,0,0) 100%)}
.hero h2{position:absolute;left:162px;top:78px;font-weight:400;font-size:38px;color:var(--white);letter-spacing:.5px}
.hero h1{position:absolute;left:162px;top:125px;font-weight:800;font-size:49px;color:var(--white)}
.hero p{position:absolute;left:162px;top:205px;width:355px;font-size:12px;font-weight:600;line-height:1.4;color:var(--white)}
.btn{display:inline-block;background:var(--green);color:var(--white);font-weight:700;border-radius:20px;text-align:center}
.hero .btn{position:absolute;left:162px;top:296px;width:150px;height:40px;line-height:40px;font-size:14px}
.hero svg{position:absolute;left:380px;top:340px}

/* section heading */
.heading{position:absolute;left:0;width:1200px;text-align:center;font-weight:800;font-size:30px;color:var(--ink)}
.heading em{font-style:normal;color:var(--green)}

/* features */
.feature{position:absolute;width:230px;text-align:center}
.feature .photo{width:137px;height:137px;border-radius:50%;margin:0 auto;border:6px solid var(--white);box-shadow:0 2px 10px rgba(0,0,0,.25)}
.feature h3{margin-top:38px;font-size:19px;font-weight:700}
.feature p{margin:12px auto 0;width:175px;font-size:11px;line-height:1.35;color:var(--muted)}

/* team band */
.band-photo{position:absolute;left:0;top:1050px;width:629px;height:405px;background:linear-gradient(160deg,#7c8590 0%,#5a4e4a 45%,#b4552f 75%,#3d3a3c 100%)}
.band-copy{position:absolute;left:629px;top:1050px;width:571px;height:405px;background:var(--navy)}
.band-copy h2{position:absolute;left:44px;top:72px;font-size:29px;font-weight:800;line-height:1.25;color:var(--white)}
.band-copy p{position:absolute;left:44px;top:164px;width:400px;font-size:12px;font-weight:600;line-height:1.4;color:var(--white)}
.btn-dark{position:absolute;left:44px;top:268px;width:132px;height:34px;line-height:34px;font-size:12px;font-weight:700;color:var(--white);background:var(--darker);border-radius:18px;text-align:center}

/* causes */
.cause{position:absolute;top:1587px;width:274px;height:368px;background:var(--card)}
.cause .photo{height:155px}
.cause .bar{position:absolute;left:24px;top:168px;width:226px;height:14px;border-radius:7px;background:var(--white)}
.cause .bar i{position:absolute;left:3px;top:4px;width:140px;height:6px;border-radius:3px;background:#444}
.cause .bar b{position:absolute;right:8px;top:1px;font-size:9px;color:#333}
.cause .figs{position:absolute;left:24px;top:200px;width:226px;display:flex;justify-content:space-between;font-size:10px;font-weight:700;color:var(--white)}
.cause h3{position:absolute;left:20px;top:240px;width:234px;text-align:center;font-size:15px;font-weight:700;line-height:1.3;color:var(--white)}
.cause .btn{position:absolute;left:82px;top:316px;width:110px;height:30px;line-height:30px;font-size:11px}

/* testimonials */
.voices{position:absolute;left:0;top:2044px;width:1200px;height:407px;background:var(--navy-deep)}
.voices .heading{top:40px;color:var(--white)}
.quote{position:absolute;left:186px;top:121px;width:828px;height:168px;background:var(--white);border-radius:8px}
.quote:after{content:"";position:absolute;left:404px;bottom:-14px;border:14px solid transparent;border-bottom:0;border-top-color:var(--white)}
.quote svg{position:absolute;left:28px;top:28px}
.quote p{position:absolute;left:75px;top:30px;width:710px;font-size:11px;line-height:1.35;color:#777}
.quote h4{position:absolute;left:0;top:112px;width:100%;text-align:center;font-size:18px;font-weight:700}
.quote h4 span{color:var(--green)}
.dots{position:absolute;left:510px;top:2368px;display:flex;gap:16px}
.dots span{width:46px;height:46px;border-radius:50%;border:3px solid var(--white);background:#6a6a72}

/* trainers */
.trainer{position:absolute;top:2568px;width:240px;text-align:center}
.trainer .photo{width:195px;height:195px;border-radius:50%;margin:0 auto;border:8px solid var(--white);box-shadow:0 2px 10px rgba(0,0,0,.25)}
.trainer h3{margin-top:22px;font-size:21px;font-weight:700;color:var(--green)}
.trainer p{font-size:15px;font-weight:700;margin-top:2px}

/* footer */
.footer{position:absolute;left:0;top:2900px;width:1200px;height:421px;background:var(--dark);color:var(--white)}
.callbar{position:absolute;left:162px;top:2860px;width:874px;height:85px;background:var(--green)}
.callbar svg{position:absolute;left:22px;top:26px}
.callbar .ask{position:absolute;left:72px;top:27px;font-size:12px;font-weight:600;line-height:1.2}
.callbar .num{position:absolute;left:178px;top:22px;font-size:31px;font-weight:800;color:var(--white)}
.callbar .field{position:absolute;left:484px;top:29px;width:240px;height:30px;border-radius:15px;background:var(--white)}
.callbar .sub{position:absolute;left:676px;top:29px;width:118px;height:30px;line-height:30px;border-radius:15px;background:var(--darker);color:var(--white);font-size:12px;font-weight:700;text-align:center}
.fbrand{position:absolute;left:162px;top:94px;display:flex;align-items:center;gap:10px;font-size:26px;font-weight:800}
.fbrand i{width:22px;height:22px;background:var(--green);display:block}
.mission h3{position:absolute;left:162px;top:168px;font-size:23px;font-weight:700}
.mission p{position:absolute;left:162px;width:300px;font-size:11px;line-height:1.4}
.col-title{position:absolute;top:94px;font-size:12px;font-weight:600}
.gallery{position:absolute;left:489px;top:126px;display:grid;grid-template-columns:112px 112px;gap:12px 10px}
.gallery span{height:90px;display:block}
.g1{background:linear-gradient(135deg,#9aa4ae,#6d7a80)}
.g2{background:linear-gradient(135deg,#b7b4a8,#7d8a8f)}
.g3{background:linear-gradient(135deg,#3a3f4a,#a0463a)}
.g4{background:linear-gradient(135deg,#6a8a52,#b07a4a)}
.contact{position:absolute;left:837px;width:220px}
.contact .pin{position:absolute;left:0;top:0;width:18px;height:18px;border-radius:50%;background:var(--green)}
.contact h4{margin-left:30px;font-size:11px;font-weight:600;color:var(--green)}
.contact p{margin-left:30px;font-size:11px;line-height:1.35;font-weight:600}
.copy{position:absolute;left:0;top:382px;width:1200px;text-align:center;font-size:11px}
</style>
</head>
<body>

<div class="topbar">
  <span class="tag">Harbo Hale Community Wellness Non-Profit</span>
  <span class="phone">+100 555 0142</span>
  <div class="social"><span class="s1"></span><span class="s2"></span><span class="s3"></span><span class="s4"></span></div>
</div>

<header class="nav">
  <div class="brand"><i></i>Harbo Hale</div>
  <nav class="menu"><span>HOME</span><span>ABOUT US</span><span>TRIPS</span><span>TRAINERS/HOSTS</span><span>REGISTER</span><span>ALBUMS</span><span>CONTACT US</span></nav>
</header>

<section class="hero" role="img" aria-label="Photo of a long line of refugees walking along a grassy hillside">
  <div class="shade"></div>
  <h2>IN HAC HABITASSE PLATEA</h2>
  <h1>CURABITUR UT FELIS</h1>
  <p>Lorem Ipsum is simply dummy text of the printing and typesetting industry. Lorem Ipsum has beenLorem Ipsum is simply dummy text of the printing and type-setting industry. Lorem Ipsum has been</p>
  <span class="btn">Donate Now</span>
  <svg width="110" height="125" viewBox="0 0 110 125"><polygon points="0,125 110,125 70,0" fill="#6dbe45" opacity=".85"/></svg>
</section>

<h2 class="heading" style="top:615px">DUIS MAURIS <em>EROS SED</em></h2>

<div class="feature" style="left:106px;top:690px"><div class="photo" role="img" aria-label="Photo of a smiling refugee child" style="background:linear-gradient(135deg,#a7b2bc,#8b6e5c)"></div><h3>Vivamus id neque</h3><p>Lorem Ipsum is simply dummy text of the printing and typesetting industry. Lorem Ipsum has been</p></div>
<div class="feature" style="left:354px;top:690px"><div class="photo" role="img" aria-label="Photo of white tents in a refugee camp" style="background:linear-gradient(135deg,#d3d6da,#7d8f9a)"></div><h3>Quisque iaculis</h3><p>Lorem Ipsum is simply dummy text of the printing and typesetting industry. Lorem Ipsum has been</p></div>
<div class="feature" style="left:600px;top:690px"><div class="photo" role="img" aria-label="Photo of a crowd of people carrying bags" style="background:linear-gradient(135deg,#4d5a78,#9a8a7a)"></div><h3>Non dignissim elit</h3><p>Lorem Ipsum is simply dummy text of the printing and typesetting industry. Lorem Ipsum has been</p></div>
<div class="feature" style="left:859px;top:690px"><div class="photo" role="img" aria-label="Photo of fresh fruit and vegetables" style="background:linear-gradient(135deg,#c43a2a,#e0a12f 50%,#5e9a3a)"></div><h3>Quisque iaculis</h3><p>Lorem Ipsum is simply dummy text of the printing and typesetting industry. Lorem Ipsum has been</p></div>

<div class="band-photo" role="img" aria-label="Photo of a volunteer helping refugee children in life jackets off a boat"></div>
<section class="band-copy">
  <h2>WE ARE<br>NON-PROFIT TEAM</h2>
  <p>Lorem ipsum dolor sit amet, consectetur adipisicing elit, sed do eiusmod tempor iont incididunt ut labore et dolore magna aliqua. Ut enim ad minim veniam, quis nostrudti exercitation ullamco laboris nisi ut aliquip ex ea commodo consequat.</p>
  <span class="btn-dark">Donate Now</span>
</section>

<h2 class="heading" style="top:1507px">FEATURED <em>CAUSES</em></h2>

<article class="cause" style="left:162px"><div class="photo" role="img" aria-label="Photo of hands sharing food" style="background:linear-gradient(135deg,#3f6e9a,#c49a6a)"></div><div class="bar"><i></i><b>30%</b></div><div class="figs"><span>Raised: $300,000</span><span>Goal: $600,000</span></div><h3>Morbi egestas luctus odio eu sollicitudin</h3><span class="btn">Donate Now</span></article>
<article class="cause" style="left:463px"><div class="photo" role="img" aria-label="Photo of a group of refugee children" style="background:linear-gradient(135deg,#8a7f7a,#3f5a4a)"></div><div class="bar"><i></i><b>30%</b></div><div class="figs"><span>Raised: $300,000</span><span>Goal: $600,000</span></div><h3>Quisque nec suscipit purus at iaculis orci</h3><span class="btn">Donate Now</span></article>
<article class="cause" style="left:762px"><div class="photo" role="img" aria-label="Photo of fresh vegetables on a table" style="background:linear-gradient(135deg,#4f7a3a,#a0542f 60%,#6a3a5a)"></div><div class="bar"><i></i><b>30%</b></div><div class="figs"><span>Raised: $300,000</span><span>Goal: $600,000</span></div><h3>Sed molestie, lectus at faucibus condimentum</h3><span class="btn">Donate Now</span></article>

<section class="voices">
  <h2 class="heading">WHAT PEOPLE SAY</h2>
  <div class="quote">
    <svg width="34" height="26" viewBox="0 0 34 26"><path d="M0 26V14C0 6 4 1 12 0v5c-4 1-6 4-6 8h6v13zM20 26V14c0-8 4-13 12-14v5c-4 1-6 4-6 8h6v13z" fill="#d6d6d6"/></svg>
    <p>Lorem ipsum dolor sit amet, consectetur adipisicing elit, sed do eiusmod tempor incididunt ut labore et dolore magna aliqua. Ut enim ad minim veniam. Quis nostrud exercitation ullamco laboris nisi ut aliquip ex ea commodo consequat. Duis aute irure dolor Lorem ipsum dolor sit amet, consectetur adipisicing elit, sed do eiusmod tempor incididunt ut labore et dolore magna aliqua. Ut enim ad minim veniam.</p>
    <h4><span>Lena</span> | Volunteer</h4>
  </div>
</section>
<div class="dots"><span role="img" aria-label="Portrait of a volunteer"></span><span role="img" aria-label="Portrait of a volunteer"></span><span role="img" aria-label="Portrait of a volunteer"></span></div>

<h2 class="heading" style="top:2502px">OUR <em>TRAINERS</em></h2>

<div class="trainer" style="left:168px"><div class="photo" role="img" aria-label="Portrait of trainer Nora Vale" style="background:linear-gradient(135deg,#c9d6e0,#b58f78)"></div><h3>NORA VALE</h3><p>Trainer</p></div>
<div class="trainer" style="left:478px"><div class="photo" role="img" aria-label="Portrait of trainer Theo Brand" style="background:linear-gradient(135deg,#6f9a5a,#e38a2f)"></div><h3>THEO BRAND</h3><p>Trainer</p></div>
<div class="trainer" style="left:794px"><div class="photo" role="img" aria-label="Portrait of volunteer Ines Moor" style="background:linear-gradient(135deg,#8a6a55,#d8c8b8)"></div><h3>INES MOOR</h3><p>Volunteer</p></div>

<footer class="footer">
  <div class="fbrand"><i></i>Harbo Hale</div>
  <div class="mission">
    <h3>OUR MISSION</h3>
    <p style="top:206px">Lorem ipsum dolor sit amet, consectetur adipisicing elit, sed do eiusmod tempor incididunt ut labore et dolore magna aliqua. Ut enim ad minim veniam.</p>
    <p style="top:272px">Quis nostrud exercitation ullamco laboris nisi ut aliquip ex ea commodo consequat. Duis aute irure dolor.</p>
  </div>
  <h4 class="col-title" style="left:489px">GALLERY</h4>
  <div class="gallery">
    <span class="g1" role="img" aria-label="Trip photo of a group exercising"></span>
    <span class="g2" role="img" aria-label="Trip photo of a camp"></span>
    <span class="g3" role="img" aria-label="Trip photo of a crowd"></span>
    <span class="g4" role="img" aria-label="Trip photo of a fitness class outdoors"></span>
  </div>
  <h4 class="col-title" style="left:837px">CONTACT US</h4>
  <div class="contact" style="top:130px"><span class="pin"></span><h4>Head Office</h4><p>Aliquam risus metus,<br>aliquet eget massa non,<br>sollicitudin</p></div>
  <div class="contact" style="top:210px"><span class="pin"></span><h4>Phone Number</h4><p>+100 555 0199<br>+100 555 0199</p></div>
  <div class="contact" style="top:288px"><span class="pin"></span><h4>Email</h4><p>help@harbohale-example.org<br>www.harbohale-example.org</p></div>
  <p class="copy">Copyright © 2017 Harbo Hale. All Rights Reserved.</p>
</footer>

<div class="callbar">
  <svg width="30" height="30" viewBox="0 0 24 24"><path d="M6.6 10.8a15.1 15.1 0 0 0 6.6 6.6l2.2-2.2c.3-.3.7-.4 1-.2 1.1.4 2.3.6 3.6.6.6 0 1 .4 1 1V20c0 .6-.4 1-1 1A17 17 0 0 1 3 4c0-.6.4-1 1-1h3.5c.6 0 1 .4 1 1 0 1.3.2 2.5.6 3.6.1.3 0 .7-.2 1z" fill="#fff"/></svg>
  <div class="ask">DO YOU HAVE<br>A QUESTION?</div>
  <div class="num">+0100 555 010</div>
  <div class="field"></div>
  <div class="sub">Subscribe</div>
</div>

</body>
</html>
```